Medical Centre Website

We need a new design for a medical centre based in Perth, Western Australia called 'Tarvin Grove Medical Centre'.

The medical centre does general practitioner work including general checkups, ecg, heart checks, woman's health and more servicing children and adults. They also do home visits on occasions where the patient cannot attend the centre.

They would like an information/brochure website where visitors can read up on the practice, send email and view their location.

The client wish the design to be clean, fresh and light. The main colours are a light purple/blue and to a dark navy blue. The client would not want the logo to be altered in any way. This includes changing the words colours or the image.

The final design should represent a loving, family friendly practice where patients can come to receive the best treatments.

We just need the end product to be presented to un in a layed psd format. The fonts must be as per the W3C standards.

**IMPORTANT**
I have received heaps of chatlink invites in the past. To treat everyone fairly, I do not add people to my chatlink list as in the past people expected us to give them the prize. If you have questions, please ask them in pixel forum as it may benefit others who are also designing the site. If I need to, I will send a message to the user.
Updates

Hi Designers,

Most designs we have received have been overly cluttered. Are you able to simplify the designs.

Cheers, Dorian

Hi Designers,

Some of the designs are quite attractive but aremore cluttered than I would like. If you have a look at the following design, the design is very simple and straight to the point. A lot of designs have too much wording and the reader can be put off. We are looking something more like:

velmoxa.com.au

I would prefer to see designs and have opened up the contest for a further 7 days.

Designers,

We have received feedback from the client and Quite frankly he don’t really like any of them.They are too cluttered and Americanised. All drab blue colours.
 
If you have a look at template monster, these designs are better and cleaner. We do not want heaps of writing on the front page.

If you look at the eariler examples such as quorbeyclinic.com.au which I did myself, the client loves that simplicity of the site.

```html
<!DOCTYPE html>
<html lang="en">
<head>
<meta charset="utf-8">
<title>Tarvin Grove Medical Centre</title>
<link href="https://fonts.googleapis.com/css2?family=Noto+Serif:wght@400;700&family=Arimo:wght@400;700&display=swap" rel="stylesheet">
<style>
:root{
  --blue:#1a7fc4;
  --blue-dark:#0a64a8;
  --blue-light:#2fc3f2;
  --brand:#4f7fc6;
  --ink:#4a4a4a;
  --ink-soft:#555555;
  --line:#cfcfcf;
  --white:#ffffff;
  --serif:"Noto Serif",Georgia,serif;
  --sans:"Arimo",Arial,sans-serif;
}
*{box-sizing:border-box;margin:0;padding:0}
html,body{width:1200px;height:1000px;overflow:hidden}
body{position:relative;background:var(--white);font-family:var(--sans);color:var(--ink)}
.site-header{position:absolute;left:0;top:0;width:1200px;height:537px;background:linear-gradient(#ffffff,#f0f0f0);border-top:3px solid #e4e4e4;border-bottom:3px solid #e3e3e3}
.brand{position:absolute;left:125px;top:32px;font-family:var(--serif);font-weight:700;font-size:27px;color:var(--brand);white-space:nowrap}
.utility{position:absolute;left:834px;top:0;width:244px;height:48px;background:#e6e6e6;border-radius:0 0 8px 8px;display:flex;justify-content:center;align-items:flex-end;padding-bottom:8px}
.utility a{display:flex;flex-direction:column;align-items:center;font-family:var(--serif);font-weight:700;font-size:10.5px;color:#666;text-decoration:none;padding:0 9px;position:relative}
.utility a+a::before{content:"|";position:absolute;left:-2px;bottom:0;color:#777}
.utility svg{width:18px;height:18px;margin-bottom:2px}
.login{position:absolute;left:713px;top:64px;display:flex;gap:10px}
.login .field{width:152px;height:28px;border:1px solid #ccc;background:#fff;font-family:var(--serif);font-size:13px;color:#666;padding:5px 10px}
.login .go{width:39px;height:27px;margin-left:1px;background:linear-gradient(#28a3e6,var(--blue-dark));color:#fff;font-family:var(--serif);font-size:13px;border-radius:2px;display:flex;align-items:center;justify-content:center}
.stage{position:absolute;left:115px;top:116px;width:964px;height:407px;border:1px solid #c8c8c8;border-radius:6px;background:#f6f6f6;box-shadow:0 1px 4px rgba(0,0,0,.25)}
.main-nav{position:absolute;left:5px;top:5px;width:952px;height:47px;background:linear-gradient(#2ea6e4,var(--blue-dark));border-radius:4px 4px 0 0;display:flex}
.main-nav a{height:47px;display:flex;align-items:center;justify-content:center;color:#fff;font-family:var(--serif);font-size:18px;text-decoration:none;border-right:1px solid #0b5d98}
.main-nav a.active{background:linear-gradient(var(--blue-light),#1893d8);position:relative}
.main-nav a.active::after{content:"";position:absolute;bottom:0;left:64px;border:6px solid transparent;border-bottom-color:#f4f4f4}
.main-nav .phone{margin-left:auto;padding-right:24px;display:flex;align-items:center;color:#fff;font-family:var(--serif);font-size:24px}
.hero{position:absolute;left:5px;top:54px;width:952px;height:346px;background:linear-gradient(100deg,#ffffff 0%,#eeeeee 30%,#f5f5f5 36%);overflow:hidden}
.hero-photo{position:absolute;left:330px;top:0;width:622px;height:346px;background:linear-gradient(90deg,#f0f0f0 0%,rgba(214,224,236,.9) 25%,#c9d3df 60%,#e8e8ea 100%)}
.hero-copy{position:absolute;left:26px;top:62px;width:262px}
.hero-title{font-family:var(--serif);font-weight:400;line-height:1;white-space:nowrap}
.hero-title .l1{font-size:42px;color:#555}
.hero-title .l1 small{font-size:19px}
.hero-title .l2{display:flex;align-items:flex-end;justify-content:space-between;margin-top:-2px}
.hero-title .l2 span:first-child{font-size:19px;color:var(--blue);margin-left:1px;margin-bottom:10px}
.hero-title .l2 span:last-child{font-size:44px;color:#2569b8}
.hero-copy p{margin-top:14px;font-size:12px;line-height:16px;text-align:justify;color:var(--ink-soft)}
.dots{position:absolute;left:27px;top:310px;display:flex;gap:7px}
.dots i{width:16px;height:16px;border-radius:50%;background:#c4c4c4;border:1px solid #b0b0b0}
.dots i.on{background:var(--blue)}
.content{position:absolute;left:117px;top:540px;width:961px;height:460px;background:#fff;border-left:1px solid #ddd;border-right:1px solid #ddd}
.card{position:absolute;top:10px;width:227px;height:279px;border:1px solid var(--line);border-radius:6px;background:linear-gradient(#fff,#ececec)}
.card h2,.feed h2{font-family:var(--serif);font-weight:400;font-size:16px;color:var(--blue);text-transform:uppercase;white-space:nowrap}
.card h2{height:37px;padding:9px 0 0 10px;border-bottom:1px solid #d6d6d6}
.card .thumb{margin:10px 0 0 10px;width:206px;height:114px;border:1px solid #ccc;background:#fff;padding:5px}
.card .thumb div{width:100%;height:100%}
.card p{margin:10px 10px 0;font-size:12px;line-height:16px;color:var(--ink-soft)}
.card p b{display:block;color:#444}
.feed p b{color:#444}
.btn{position:absolute;left:10px;bottom:9px;height:23px;padding:0 9px;border-radius:4px;background:linear-gradient(#2a9ee0,var(--blue-dark));color:#fff;font-family:var(--serif);font-size:13px;display:flex;align-items:center}
.btn.dark{background:linear-gradient(#777,#444)}
.feeds{position:absolute;left:10px;top:299px;width:938px;height:200px;border:1px solid var(--line);border-radius:6px;background:#fff}
.feeds::after{content:"";position:absolute;left:474px;top:20px;height:180px;border-left:1px dotted #999}
.feed{position:absolute;top:15px}
.event{position:relative;height:80px;margin-top:16px}
.event .thumb{position:absolute;left:0;top:0;width:106px;height:84px;border:1px solid #ccc;background:#fff;padding:5px}
.event .thumb div{width:100%;height:100%}
.event .date{position:absolute;left:119px;top:2px;font-family:var(--serif);font-size:13px;color:#666}
.feed p{font-size:12px;line-height:16px;color:var(--ink-soft)}
.feed p a{font-family:var(--serif);font-weight:700;font-size:13px;color:var(--blue-dark);text-decoration:none}
.event p{position:absolute;left:120px;top:23px;width:320px}
.news{position:relative;height:65px;margin-top:20px}
.news .day{position:absolute;left:-1px;top:0;width:46px;height:38px;border-radius:3px;background:linear-gradient(#2aa3e3,var(--blue-dark));color:#fff;font-family:var(--serif);font-size:20px;display:flex;align-items:center;justify-content:center}
.news .month{position:absolute;left:60px;top:4px;font-family:var(--serif);font-size:13px;color:var(--blue-dark)}
.news p{position:absolute;left:61px;top:24px;width:350px}
</style>
</head>
<body>
<header class="site-header">
  <div class="brand">Tarvin Grove Medical Centre</div>
  <nav class="utility">
    <a href="#"><svg viewBox="0 0 18 18"><circle cx="9" cy="9" r="8" fill="#666"/><rect x="7.5" y="5" width="3" height="8" rx="1" fill="#ddd"/></svg>Sign-up</a>
    <a href="#"><svg viewBox="0 0 18 18"><path d="M2 9 9 3l7 6M4 8v8h4v-4h2v4h4V8" fill="none" stroke="#666" stroke-width="1.6"/></svg>Home</a>
    <a href="#"><svg viewBox="0 0 18 18" fill="none" stroke="#666" stroke-width="1.4"><rect x="7" y="2" width="4" height="3"/><rect x="2" y="13" width="4" height="3"/><rect x="7" y="13" width="4" height="3"/><rect x="12" y="13" width="4" height="3"/><path d="M9 5v8M4 13V9h10v4"/></svg>Sitemap</a>
    <a href="#"><svg viewBox="0 0 18 18" fill="none" stroke="#666" stroke-width="1.5"><rect x="2" y="4" width="14" height="10"/><path d="m2 4 7 6 7-6"/></svg>Contact</a>
  </nav>
  <form class="login">
    <div class="field">user name:</div>
    <div class="field">password:</div>
    <div class="go">GO</div>
  </form>
  <div class="stage">
    <nav class="main-nav">
      <a href="#" class="active" style="width:140px">Home</a>
      <a href="#" style="width:171px">Company</a>
      <a href="#" style="width:166px">Carreers</a>
      <a href="#" style="width:174px">Contact us</a>
      <span class="phone">1-800-555-0142</span>
    </nav>
    <section class="hero">
      <div class="hero-photo" role="img" aria-label="Photo of a clinician in mask and gloves examining a test tube"></div>
      <div class="hero-copy">
        <h1 class="hero-title">
          <div class="l1">CARING <small>FOR YOUR</small></div>
          <div class="l2"><span>WHOLE</span><span>FAMILY</span></div>
        </h1>
        <p>Our friendly general practitioners look after children and adults alike, from routine checkups and heart tests to women's health. When you cannot come to us, our doctors can visit you at home across Perth.</p>
      </div>
      <div class="dots"><i></i><i class="on"></i><i></i><i></i><i></i></div>
    </section>
  </div>
</header>

<main class="content">
  <article class="card" style="left:10px">
    <h2>General Checkups</h2>
    <div class="thumb"><div role="img" aria-label="Photo of a team of doctors and nurses" style="background:linear-gradient(#f4f4f4,#d7dde4)"></div></div>
    <p><b>Care for every age</b>Regular health checks for children and adults with our caring family doctors.</p>
    <span class="btn dark">Read More</span>
  </article>
  <article class="card" style="left:247px">
    <h2>Heart &amp; ECG</h2>
    <div class="thumb"><div role="img" aria-label="Photo of a doctor talking with patients" style="background:linear-gradient(#f6f6f6,#c9b9ad)"></div></div>
    <p><b>Heart health checks</b>Fast ECG testing and blood pressure reviews done right here in the practice.</p>
    <span class="btn">Read More</span>
  </article>
  <article class="card" style="left:484px">
    <h2>Women's Health</h2>
    <div class="thumb"><div role="img" aria-label="Photo of a clinician holding a test tube beside a rack" style="background:linear-gradient(90deg,#dfe6e3,#e8d7c6)"></div></div>
    <p><b>Support you can trust</b>Screening, pregnancy care and advice in a calm and private setting.</p>
    <span class="btn">Read More</span>
  </article>
  <article class="card" style="left:721px">
    <h2>Home Visits</h2>
    <div class="thumb"><div role="img" aria-label="Photo of a doctor visiting a patient at home" style="background:linear-gradient(#eef0f3,#b9c3cf)"></div></div>
    <p><b>Care at your door</b>When you cannot attend the centre, one of our doctors can come to you.</p>
    <span class="btn">Read More</span>
  </article>

  <section class="feeds">
    <div class="feed" style="left:10px;width:450px">
      <h2>Health Clinics</h2>
      <div class="event">
        <div class="thumb"><div role="img" aria-label="Photo of a doctor examining a patient" style="background:linear-gradient(#eef0f2,#c8ccd2)"></div></div>
        <span class="date">20 October 2011</span>
        <p><b>Flu vaccination clinic</b> open for all ages. Walk in on weekday mornings or book a time that suits your family with our reception team <a href="#">Read More</a></p>
      </div>
      <div class="event">
        <div class="thumb"><div role="img" aria-label="Photo of a children's health clinic" style="background:linear-gradient(#eef0f2,#c8ccd2)"></div></div>
        <span class="date">20 October 2011</span>
      </div>
    </div>
    <div class="feed" style="left:514px;top:20px;width:420px">
      <h2>Practice News</h2>
      <div class="news">
        <span class="day">20</span>
        <span class="month">October 2011</span>
        <p><b>Extended opening hours</b> now on Saturdays. Our doctors are available for checkups, heart tests and women's health appointments <a href="#">Read More</a></p>
      </div>
      <div class="news">
        <span class="day">20</span>
        <span class="month">October 2011</span>
      </div>
    </div>
  </section>
</main>
</body>
</html>
```